Bref créative |
Website for Kelp Harbour | ||
Kelp Harbour | ||
Massage Therapy | ||
www.kelpharbour.co.uk (not live yet) | ||
Friendly and professional mobile massage therapy company. Offer a range of massage types such as holistic, remedial, deep tissue and sports. Also offer postural assessments, range of movement and joint tests Work with corporate and private clients, sports teams and charities |
Dislike....Anything too masculine or too feminine Too much clutter on web pages Imbalance between amount of text and images To much industry speak Like...plenty of white space positive and energetic text and images clear and concise text, without jargon Making clients feel comfortable and the company feel approachable |
Cutting-Edge Unique/Creative Clean/Simple Professional Trendy Friendly Exciting Modern Colorful Elegant |
White | ||
Dark Blue/Indigo | ||
Light/Mint Green | ||
top | ||
http://www.quorvastudio.com/ | ||
http://plw-tandor.com/ | ||
http://www.vestoria.co.uk/spa.html | ||
• Additional Comments were - I like QuorvaStudio use of white space and their balance between text and images. They also use Plain English which i think makes clients comfortable and they appear approachable. Vestoria Spa feels very elegant in its design and I like the simple navigation. PLW Tandor I like the way in they break information down about massage itself, making it easy to read and digest. Their actual design though I think could be better. • Logo and contact details are to appear on every page |

```html
<!DOCTYPE html>
<html lang="en">
<head>
<meta charset="utf-8">
<title>Kelp Harbour Massage Therapy</title>
<link href="https://fonts.googleapis.com/css2?family=Open+Sans:wght@400;600;700&display=swap" rel="stylesheet">
<style>
:root{
  --indigo:#1f3566;
  --green:#79b487;
  --green-dark:#5e9b6d;
  --mint:#e4f1e7;
  --text:#4a4f57;
  --muted:#8a9098;
  --white:#ffffff;
}
*{box-sizing:border-box;margin:0;padding:0}
html,body{width:1200px;height:997px;overflow:hidden}
body{font-family:"Open Sans",Arial,sans-serif;color:var(--text);font-size:11px;line-height:1.45;
  background:linear-gradient(180deg,var(--mint) 0,#f7fbf8 380px,var(--white) 560px,var(--white) 100%);position:relative}
.page{position:absolute;left:278px;top:0;width:640px;height:997px}
.abs{position:absolute}
.nowrap{white-space:nowrap}

/* header */
.brand{left:0;top:26px;color:var(--indigo);font-weight:700;font-size:28px;line-height:1;white-space:nowrap}
.btn-appoint{left:360px;top:16px;width:120px;height:20px;background:var(--green);color:var(--white);font-size:9px;
  text-align:center;line-height:20px;border-radius:2px;white-space:nowrap}
.contact-with{left:540px;top:22px;font-size:8px;color:var(--muted);display:flex;gap:3px;align-items:center;white-space:nowrap}
.contact-with i{display:inline-block;width:8px;height:8px;background:var(--indigo);border-radius:1px}
.nav{left:180px;top:60px;width:460px;height:26px;background:var(--green);display:flex;border-radius:2px}
.nav a{flex:1;color:var(--white);font-size:9px;text-align:center;line-height:26px;text-decoration:none;white-space:nowrap;border-right:1px solid rgba(255,255,255,.35)}
.nav a:last-child{border-right:0}
.nav a.current{background:var(--green-dark)}

/* hero */
.hero-title{left:0;top:128px;font-size:26px;color:var(--green);font-weight:400;white-space:nowrap}
.hero-sub{left:0;top:168px;font-size:13px;color:var(--indigo);font-weight:700;white-space:nowrap}
.hero-text{left:0;top:196px;font-size:12px;color:var(--indigo);white-space:nowrap}
.hero-q{left:0;top:220px;font-size:12px;color:var(--green-dark);font-weight:600;white-space:nowrap}
.btn-small{background:var(--green);color:var(--white);font-size:8px;padding:0 8px;height:17px;line-height:17px;border-radius:2px;white-space:nowrap}
.hero-btn{left:0;top:268px}
.hero-img{left:355px;top:150px;width:285px;height:185px;background:linear-gradient(160deg,#eef3ef 0,#dfe6e3 60%,#c9d3cf 100%)}
.dots{left:588px;top:326px;display:flex;gap:3px}
.dots span{width:7px;height:7px;border:1px solid #b9c4bd;background:var(--white)}
.dots span.on{background:var(--green)}

/* service cards */
.cards{left:0;top:346px;width:640px;height:218px;display:flex;gap:5px}
.card{flex:1;background:var(--mint);border:1px solid #d5e7d9;padding:0 0 8px}
.card h3{background:var(--green);color:var(--white);font-size:14px;font-weight:400;text-align:center;height:28px;line-height:28px}
.card .photo{margin:6px 8px;height:98px;background:linear-gradient(135deg,#e7c9b0,#c89676)}
.card p{margin:0 10px;font-size:8.5px;line-height:1.35}
.card .btn-small{display:inline-block;margin:8px 10px 0}

/* welcome */
.welcome-title{left:0;top:582px;font-size:18px;color:var(--green);font-weight:400;white-space:nowrap}
.welcome-title b{color:var(--indigo);font-weight:700}
.welcome-img{left:0;top:618px;width:140px;height:112px;background:linear-gradient(135deg,#e0b99c,#b58565)}
.welcome-intro{left:152px;top:616px;width:282px;font-size:9px}
.welcome-intro p+p{margin-top:6px}
.welcome-body{left:0;top:748px;width:434px;font-size:9px}
.welcome-body p{margin-bottom:9px}
.ticks{list-style:none}
.ticks li{display:flex;align-items:center;gap:6px;height:14px}
.ticks svg{width:9px;height:9px}

/* sidebar */
.side{left:457px;top:576px;width:183px}
.side h4{font-size:18px;color:var(--green);font-weight:400;line-height:1.2;white-space:nowrap}
.side h4 b{color:var(--indigo);font-weight:600}
.side p{font-size:9px;margin:4px 0 10px}
.phone{display:flex;align-items:center;gap:6px;font-size:12px;color:var(--indigo);font-weight:600;margin-bottom:14px;white-space:nowrap}
.phone em{font-style:normal;color:var(--green-dark)}
.hours{font-size:9px;color:var(--indigo);margin:4px 0 14px}

/* footer */
.footer-rule{left:0;top:950px;width:640px;height:1px;background:#d6e2d9}
.footer-copy{left:0;top:958px;font-size:8px;color:var(--muted);white-space:nowrap}
</style>
</head>
<body>
<div class="page">
  <header>
    <div class="abs brand">Kelp Harbour</div>
    <div class="abs btn-appoint">Request an appointment</div>
    <div class="abs contact-with">Contact with us <i></i><i></i><i></i></div>
    <nav class="abs nav">
      <a class="current">HOME</a><a>ABOUT US</a><a>PRICES</a><a>SERVICES</a><a>LOCATION</a><a>TESTIMONIALS</a><a>CONTACT</a>
    </nav>
  </header>

  <section class="hero">
    <h1 class="abs hero-title">Welcome to</h1>
    <div class="abs hero-sub">Kelp Harbour Massage Therapy</div>
    <div class="abs hero-text">Lorem Ipsum is simply dummy text of the printing</div>
    <div class="abs hero-q">Are you suffering from pain, muscle injury or stress?</div>
    <div class="abs btn-small hero-btn">Book an appointment</div>
    <div class="abs hero-img" role="img" aria-label="Therapist giving a stretching massage to a client"></div>
    <div class="abs dots"><span class="on"></span><span></span><span></span></div>
  </section>

  <section class="abs cards">
    <article class="card"><h3>Holistic</h3><div class="photo" role="img" aria-label="Holistic massage with stones"></div>
      <p>Lorem Ipsum is simply dummy text of the printing and typesetting industry.</p><span class="btn-small">» Read more</span></article>
    <article class="card"><h3>Remedial</h3><div class="photo" role="img" aria-label="Remedial massage on a client's back"></div>
      <p>Lorem Ipsum is simply dummy text of the printing and typesetting industry.</p><span class="btn-small">» Read more</span></article>
    <article class="card"><h3>Deep tissue</h3><div class="photo" role="img" aria-label="Deep tissue massage on shoulders"></div>
      <p>Lorem Ipsum is simply dummy text of the printing and typesetting industry.</p><span class="btn-small">» Read more</span></article>
    <article class="card"><h3>Sports</h3><div class="photo" role="img" aria-label="Active client exercising with dumbbells"></div>
      <p>Lorem Ipsum is simply dummy text of the printing and typesetting industry.</p><span class="btn-small">» Read more</span></article>
  </section>

  <section class="welcome">
    <h2 class="abs welcome-title">Welcome to <b>Kelp Harbour</b></h2>
    <div class="abs welcome-img" role="img" aria-label="Client relaxing during a back massage"></div>
    <div class="abs welcome-intro">
      <p>Friendly and professional mobile massage therapy company. Offer a range of massage types such as holistic, remedial, deep tissue and sports.</p>
      <p>Also offer postural assessments, range of movement and joint tests. Work with corporate and private clients, sports teams and charities.</p>
      <p>Work with corporate and private clients, sports teams and charities.</p>
    </div>
    <div class="abs welcome-body">
      <p>Friendly and professional mobile massage therapy company.<br>Offer a range of massage types such as holistic, remedial, deep tissue and sports.</p>
      <p>The Massage Centre is a professional massage clinic, specialising in sports and remedial massage. We treat:</p>
      <ul class="ticks">
        <li><svg viewBox="0 0 10 10"><path d="M1 5l3 3 5-7" fill="none" stroke="#1f3566" stroke-width="2"/></svg>Back &amp; Neck pain</li>
        <li><svg viewBox="0 0 10 10"><path d="M1 5l3 3 5-7" fill="none" stroke="#1f3566" stroke-width="2"/></svg>Aches &amp; Pain</li>
        <li><svg viewBox="0 0 10 10"><path d="M1 5l3 3 5-7" fill="none" stroke="#1f3566" stroke-width="2"/></svg>Repetitive Strain</li>
        <li><svg viewBox="0 0 10 10"><path d="M1 5l3 3 5-7" fill="none" stroke="#1f3566" stroke-width="2"/></svg>Muscle &amp; Joint Stiffness</li>
        <li><svg viewBox="0 0 10 10"><path d="M1 5l3 3 5-7" fill="none" stroke="#1f3566" stroke-width="2"/></svg>Sports Injuries</li>
        <li><svg viewBox="0 0 10 10"><path d="M1 5l3 3 5-7" fill="none" stroke="#1f3566" stroke-width="2"/></svg>Postural Problems</li>
        <li><svg viewBox="0 0 10 10"><path d="M1 5l3 3 5-7" fill="none" stroke="#1f3566" stroke-width="2"/></svg>Tension Headaches</li>
      </ul>
    </div>
  </section>

  <aside class="abs side">
    <h4>Kelp Harbour</h4>
    <p>Lorem Ipsum is simply dummy text of the printing and typesetting industry.</p>
    <div class="phone"><svg width="16" height="14" viewBox="0 0 16 14"><path d="M1 4c0-2 3-3 7-3s7 1 7 3v1h-4V3.5H5V5H1z M3 7h10l1 6H2z" fill="#1f3566"/><circle cx="8" cy="10" r="1.6" fill="#fff"/></svg><span>Call us : <em>000 1234 5678</em></span></div>
    <h4>Opening <b>Hours</b></h4>
    <div class="hours">Mon-Fri: 9am-6pm<br>Sat: 9am-6pm Sun: 10am-4pm</div>
    <h4>Location</h4>
    <p>Lorem Ipsum is simply dummy text of the printing and typesetting industry. Lorem Ipsum has been the industry's standard dummy text ever since the 1500s.</p>
  </aside>

  <footer>
    <div class="abs footer-rule"></div>
    <div class="abs footer-copy">Copyright © 2013 · kelpharbour.co.uk</div>
  </footer>
</div>
</body>
</html>
```